Northway Trade Partners Needs a FRESH website

We would like a creative minded designer to take on the task to Re-design our website. Its a simple 5-7 pages. With no cart, no complex html. Just plain information about our company and products we import and export. Pictures added to the product section. Since Our logo its Blue, we would like the designer to use complementing colors in order to make the website look cleaner and modern.

Target Market(s)

The target audience will be companies looking to purchase plastic related products. Companies looking to purchase large quantities of plastic containers (Shampoo bottles, caps, sprayers, mist sprayers, cosmetic containers etc).

Industry/Entity Type

It Company

Font styles to use
Sans Serif

Requirements
Must have
• We have a section in which we would like to add pictures of some of the products we carry, therefore having an easy and clean way to navigate through the pictures will be a plus.

```html
<!DOCTYPE html>
<html lang="en">
<head>
<meta charset="utf-8">
<title>Northway Trade Partners</title>
<link href="https://fonts.googleapis.com/css2?family=Arimo:wght@400;700&family=Questrial&display=swap" rel="stylesheet">
<style>
:root{
  --brand:#0a96d8;
  --brand-dark:#1567b0;
  --nav:#1a7fc4;
  --page:#f3f3f3;
  --ink:#222;
  --text:#595959;
  --rule:#c9c9c9;
  --footer:#e3e3e3;
}
*{margin:0;padding:0;box-sizing:border-box}
html,body{width:943px;height:1200px;overflow:hidden}
body{position:relative;background:var(--page);font-family:"Arimo",Arial,sans-serif;color:var(--text)}
.topbar{position:absolute;left:0;top:0;width:943px;height:15px;background:var(--brand)}
.brand{position:absolute;display:flex;align-items:center;gap:8px;color:var(--brand);font-family:"Questrial",sans-serif}
.brand-dot{border-radius:50%;background:var(--brand);flex:none}
.brand--header{left:57px;top:33px}
.brand--header .brand-dot{width:60px;height:60px}
.brand--header .brand-name{font-size:19px;width:150px;line-height:1.15}
.brand--footer{left:732px;top:1131px}
.brand--footer .brand-dot{width:44px;height:44px}
.brand--footer .brand-name{font-size:14px;width:100px;line-height:1.15}
.contact-mail{position:absolute;right:60px;top:34px;font-size:11px;color:#8a8a8a}
.nav a{position:absolute;top:61px;font-size:11px;color:var(--nav);text-decoration:none}
.nav .is-active{left:364px;top:55px;width:56px;height:24px;line-height:24px;text-align:center;background:var(--brand);color:#fff;border-radius:2px}
.hero{position:absolute;left:55px;top:111px;width:829px;height:397px;overflow:hidden}
.hero-photo{position:absolute;inset:0;background:
  linear-gradient(90deg,rgba(255,255,255,.35) 0,rgba(255,255,255,0) 50%),
  linear-gradient(180deg,rgba(240,242,244,1) 0,rgba(230,232,234,.9) 30%,rgba(230,232,234,0) 60%),
  linear-gradient(100deg,#e8541a 0,#f39a1c 20%,#f6c62a 38%,#e9e4d2 48%,#2b5fd6 60%,#3c78e0 72%,#1d8c78 86%,#136d5c 100%)}
.hero-title{position:absolute;left:14px;top:148px;font-family:"Questrial",sans-serif;font-size:34px;font-weight:400;color:var(--ink)}
.hero-text{position:absolute;left:15px;top:198px;width:360px;font-size:13px;line-height:19px;color:#1e1e1e}
.hero-btn{position:absolute;left:15px;top:272px;width:123px;height:35px;line-height:33px;text-align:center;background:var(--brand);border-bottom:3px solid #0a6fa8;color:#fff;font-size:14px}
.services{position:absolute;left:54px;top:508px;width:830px;height:98px;background:linear-gradient(180deg,#3d9fd8,#8ccaea)}
.service{position:absolute;top:6px;width:142px;text-align:center;color:#fff;font-size:12.5px}
.service-thumb{display:block;width:123px;height:55px;margin:6px auto 0;border:2px solid #fff;border-radius:3px;box-shadow:0 1px 2px rgba(0,0,0,.3)}
.service.is-active{left:61px;top:-2px;height:93px;background:#fff;border-radius:3px;color:var(--nav);padding-top:8px}
.service.is-active::before{content:"";position:absolute;left:51px;top:-16px;border:16px solid transparent;border-top:0;border-bottom-color:#fff;border-left-width:20px;border-right-width:20px}
.rule{position:absolute;left:54px;width:829px;height:1px;background:var(--rule)}
.col{position:absolute;top:656px;width:244px}
.col-head{font-size:16.5px;font-weight:700;color:var(--brand-dark);padding:5px 0 10px;border-bottom:1px solid var(--rule);letter-spacing:.2px}
.col-head span,.more span,.gallery-head span{margin-right:12px;font-weight:400}
.col p{font-size:10.5px;line-height:17.3px;margin-top:20px}
.checklist{list-style:none;margin-top:20px}
.checklist li{position:relative;padding-left:24px;font-size:10.5px;line-height:12.5px;margin-bottom:11px}
.checklist li::before{content:"✓";position:absolute;left:0;top:0;width:13px;height:13px;background:#ddd;border:1px solid #bbb;font-size:10px;line-height:12px;text-align:center;color:#555}
.bullets{list-style:none}
.bullets li{position:relative;padding-left:31px;font-size:10.5px;line-height:17.3px}
.bullets li::before{content:"•";position:absolute;left:0;font-size:8px}
.more{position:absolute;top:877px;font-size:11px;font-weight:700;color:var(--brand-dark)}
.more span{color:var(--ink);margin-right:10px}
.gallery-head{position:absolute;left:54px;top:925px;font-size:16.5px;font-weight:700;color:var(--ink)}
.product{position:absolute;top:957px;width:186px;height:116px;overflow:hidden}
.product-photo{position:absolute;inset:0}
.product-view{position:absolute;right:0;bottom:0;width:54px;height:18px;line-height:18px;text-align:center;background:#2794d0;color:#fff;font-size:10.5px;font-weight:700}
.footer{position:absolute;left:0;top:1113px;width:943px;height:87px;background:var(--footer)}
.footer-text{position:absolute;left:55px;top:26px;font-size:10.5px;line-height:17.5px;color:#555}
</style>
</head>
<body>
<div class="topbar"></div>

<div class="brand brand--header"><span class="brand-dot"></span><span class="brand-name">Northway Trade Partners</span></div>
<div class="contact-mail">info@northwaytrade.com</div>
<nav class="nav">
  <a class="is-active" href="#">HOME</a>
  <a href="#" style="left:454px">ABOUT US</a>
  <a href="#" style="left:555px">PRODUCTS</a>
  <a href="#" style="left:661px">MISSION STATEMENT</a>
  <a href="#" style="left:815px">CONTACT US</a>
</nav>

<section class="hero">
  <div class="hero-photo" role="img" aria-label="Plastic bottles, caps and a trigger sprayer over colourful plastic pellets"></div>
  <h1 class="hero-title">Northway Trade Partners</h1>
  <p class="hero-text">Lorem Ipsum is simply dummy text of the printing and typese industry. Lorem Ipsum has been the industry's standard dum text. ever since the 1500s ending.</p>
  <div class="hero-btn">Learn More</div>
</section>

<section class="services">
  <div class="service is-active">Product Research<span class="service-thumb" role="img" aria-label="Plastic containers and sprayer" style="background:linear-gradient(100deg,#e8541a,#f6c62a 35%,#eef0f2 55%,#2b5fd6 80%,#f2d21c)"></span></div>
  <div class="service" style="left:236px">Packaging<span class="service-thumb" role="img" aria-label="Open cardboard box" style="background:linear-gradient(180deg,#eeeeee 0,#c7954e 30%,#8a5a28 60%,#d8d8d8 100%)"></span></div>
  <div class="service" style="left:414px">Product Design<span class="service-thumb" role="img" aria-label="Technical drawing with calipers" style="background:linear-gradient(135deg,#f4f5f6,#c9ced3 55%,#8d949a)"></span></div>
  <div class="service" style="left:582px">Frieght Forwarding<span class="service-thumb" role="img" aria-label="Cargo plane, truck and globe" style="background:linear-gradient(120deg,#f2f4f7 0,#9db8d8 30%,#1f4fa8 55%,#3a8fd8 75%,#e8e4dc 100%)"></span></div>
</section>

<div class="rule" style="top:642px"></div>

<section class="col" style="left:54px">
  <h2 class="col-head"><span>→</span>ABOUT US</h2>
  <p>Northway Trade Partners will be your first and last stop for sourcing products from all over the world, specifically Asia and South America.<br>We have partners all around the globe that helps us make the best decision in sourcing a product from and to any market.</p>
</section>
<section class="col" style="left:347px">
  <h2 class="col-head"><span>→</span>OUR MISSION</h2>
  <ul class="checklist">
    <li>As easy as that sounds there are many details that goes into a importing a product to your final destination.</li>
    <li>That is when Northway Trade Partners steps in as being a trustworthy company that can help you grow as a business.</li>
    <li>We will take care of all the headaches from dealing with unknown companies and make it right the first time you do business with a foreign company.</li>
  </ul>
</section>
<section class="col" style="left:639px">
  <h2 class="col-head"><span>→</span>PRODUCTS</h2>
  <p style="margin-bottom:0">Not only in the plastic industry, but here are some of the products we are currently sourcing:</p>
  <ul class="bullets">
    <li>Acrylic products</li>
    <li>Lights and lighting, LED, flashlights etc.</li>
    <li>Floor, wall ceramic, glass and porcelain tiles</li>
    <li>Marble, granite</li>
    <li>Doors: wood, steel</li>
    <li>Flooring</li>
    <li>Building supplies</li>
  </ul>
</section>
<a class="more" style="left:54px"><span>→</span>READ MORE</a>
<a class="more" style="left:639px"><span>→</span>VIEW ALL</a>

<div class="rule" style="top:906px"></div>
<h2 class="gallery-head"><span>→</span>PRODUCTS WE IMPORT</h2>

<div class="product" style="left:54px"><div class="product-photo" role="img" aria-label="Clear acrylic table with flowers" style="background:linear-gradient(180deg,#fafafa 0,#e9eaeb 45%,#c4c6c8 70%,#2a2a2a 90%,#d9d9d9 100%)"></div><span class="product-view">VIEW →</span></div>
<div class="product" style="left:269px"><div class="product-photo" role="img" aria-label="Kitchen with granite countertop" style="background:linear-gradient(180deg,#e6d7ad 0,#c9a86a 30%,#7a5a34 55%,#4b4038 75%,#2f2a26 100%)"></div><span class="product-view">VIEW →</span></div>
<div class="product" style="left:483px"><div class="product-photo" role="img" aria-label="Steel injection mould" style="background:linear-gradient(160deg,#ffffff 0,#ffffff 12%,#a9adb1 30%,#6d7276 55%,#4d5256 75%,#ffffff 92%)"></div><span class="product-view">VIEW →</span></div>
<div class="product" style="left:698px"><div class="product-photo" role="img" aria-label="Yellow and white trigger sprayer" style="background:linear-gradient(100deg,#ffffff 0,#f4d21a 25%,#f8e060 45%,#f0f0f0 65%,#ffffff 100%)"></div><span class="product-view">VIEW →</span></div>

<footer class="footer">
  <div class="footer-text">Copyright © 2014 Northway Trade Partners LLC, unless otherwise noted.<br>site map | privacy policy | disclaimer</div>
</footer>
<div class="brand brand--footer"><span class="brand-dot"></span><span class="brand-name">Northway Trade Partners</span></div>
</body>
</html>
```